New bussiness card, using company logo.
Lachlan Voss
Manager/Director
Birch Property Developments
Po Box 4657
Thuringowa Central
Qld
0455 386 218
lachlan@birchpropertydevelopments
eye catching, vibrant colours, professional

```html
<!DOCTYPE html>
<html lang="en">
<head>
<meta charset="utf-8">
<title>Birch Property Developments — Business Card</title>
<link rel="stylesheet" href="https://fonts.googleapis.com/css2?family=Arimo:wght@400;700&display=swap">
<style>
  :root {
    --stage: #161616;
    --stage-light: #262626;
    --card-white: #ffffff;
    --brand-green: #6cbf3c;
    --brand-green-light: #9ccf4a;
    --brand-green-dark: #4fa32c;
    --brand-red: #d8262c;
    --ink: #333333;
    --ink-soft: #555555;
    --panel: #2f2f2f;
  }
  * { box-sizing: border-box; margin: 0; padding: 0; }
  html, body { width: 1200px; height: 900px; overflow: hidden; }
  body {
    background: radial-gradient(ellipse at 50% 40%, var(--stage-light), var(--stage) 70%);
    font-family: "Arimo", Arial, sans-serif;
    position: relative;
  }
  .card {
    position: absolute;
    width: 520px;
    height: 318px;
    border-radius: 4px;
    overflow: hidden;
    box-shadow: 0 14px 30px rgba(0,0,0,0.6);
  }
  .card--front { left: 50px; top: 180px; background: var(--card-white); }
  .card--back {
    left: 630px; top: 180px;
    background: linear-gradient(160deg, var(--brand-green-light), var(--brand-green) 60%, var(--brand-green-dark));
  }
  .wordmark {
    display: flex; align-items: center; gap: 8px;
    color: var(--brand-red);
    font-weight: 700;
    white-space: nowrap;
  }
  .wordmark__mark { width: 12px; height: 12px; background: var(--brand-red); flex: none; }
  .card--front .wordmark { position: absolute; left: 30px; top: 62px; font-size: 17px; }
  .card--front .card__rule { position: absolute; left: 30px; top: 92px; width: 240px; height: 3px; background: var(--brand-red); }
  .holder { position: absolute; right: 34px; top: 44px; text-align: right; }
  .holder__name { color: var(--brand-green); font-weight: 700; font-size: 19px; }
  .holder__role { color: var(--ink-soft); font-size: 12px; margin-top: 4px; }
  .contact { position: absolute; left: 30px; top: 178px; color: var(--ink); font-size: 12.5px; line-height: 1.35; }
  .contact__company { font-weight: 700; text-transform: uppercase; margin-bottom: 6px; }
  .contact__lines { margin-bottom: 8px; }
  .contact__row { display: flex; align-items: center; gap: 8px; }
  .contact__icon { width: 14px; height: 14px; flex: none; }
  .card__corner {
    position: absolute; right: 0; bottom: 10px; width: 300px; height: 130px;
    background: linear-gradient(160deg, rgba(108,191,60,0) 35%, rgba(108,191,60,0.25) 100%);
  }
  .card__band { position: absolute; left: 0; right: 0; bottom: 0; height: 10px; background: var(--brand-green); }
  .card__glow {
    position: absolute; inset: 0;
    background: linear-gradient(200deg, rgba(255,255,255,0.18), rgba(255,255,255,0) 55%);
  }
  .card--back .wordmark { position: absolute; right: 40px; top: 150px; font-size: 24px; }
  .card--back .card__rule { position: absolute; right: 40px; top: 188px; width: 290px; height: 3px; background: var(--brand-red); }
  .logo-panel {
    position: absolute; left: 585px; top: 752px; width: 450px; height: 148px;
    background: var(--panel); border-radius: 8px 8px 0 0;
    display: flex; flex-direction: column; align-items: center; justify-content: center; gap: 10px;
  }
  .logo-panel .wordmark { font-size: 26px; }
  .logo-panel__rule { width: 360px; height: 4px; background: var(--brand-red); }
</style>
</head>
<body>
  <section class="card card--front" aria-label="Business card front">
    <div class="wordmark"><span class="wordmark__mark"></span><span>Birch Property Developments</span></div>
    <div class="card__rule"></div>
    <div class="holder">
      <div class="holder__name">Lachlan Voss</div>
      <div class="holder__role">Manager/Director</div>
    </div>
    <div class="contact">
      <div class="contact__company">Birch Property Developments</div>
      <div class="contact__lines">Po Box 4657<br>Banksia Heights, Qld</div>
      <div class="contact__row">
        <svg class="contact__icon" viewBox="0 0 14 14" aria-hidden="true"><circle cx="7" cy="7" r="7" fill="#6cbf3c"/><path d="M4.5 3.5l1.5 0 .7 2-1 .8a5 5 0 0 0 2 2l.8-1 2 .7v1.5c0 .5-.5 1-1 1A6.5 6.5 0 0 1 3.5 4.5c0-.5.5-1 1-1z" fill="#fff"/></svg>
        <span>0455 386 218</span>
      </div>
      <div class="contact__row">
        <svg class="contact__icon" viewBox="0 0 14 14" aria-hidden="true"><circle cx="7" cy="7" r="7" fill="#6cbf3c"/><rect x="3.5" y="4.5" width="7" height="5" fill="none" stroke="#fff" stroke-width="1"/><path d="M3.5 4.5L7 7.3l3.5-2.8" fill="none" stroke="#fff" stroke-width="1"/></svg>
        <span>lachlan@birchpropertydevelopments.au</span>
      </div>
    </div>
    <div class="card__corner" role="img" aria-label="Decorative rooftop artwork area"></div>
    <div class="card__band"></div>
  </section>

  <section class="card card--back" aria-label="Business card back">
    <div class="card__glow" role="img" aria-label="Faint rooftop artwork area"></div>
    <div class="wordmark"><span class="wordmark__mark"></span><span>Birch Property Developments</span></div>
    <div class="card__rule"></div>
  </section>

  <section class="logo-panel" aria-label="Company name">
    <div class="wordmark"><span class="wordmark__mark"></span><span>Birch Property Developments</span></div>
    <div class="logo-panel__rule"></div>
  </section>
</body>
</html>
```